Super elegant, crisp & clean Business card design required

We recently upgraded our branding - which is on our website - tavolenstudio.com

I would like a simple, yet elegant, clean business card design please.

The font of my logo is Cinzel - and because of the natural colour - it's best to have this on a black background.

I would like to have the back of the business card - with simply my logo.

PLEASE DO NOT SUBMIT A COMPLICATED / UNCLEAN DESIGN

Industry/Entity Type

Business

Contact Information for Business Card

Danvir Okelowa Photography

Font styles to use
Other font styles liked:
• Cinzel

Requirements
Must have
• A backpage with nothing but my logo
• Simple design - stands out
Should not have
• Colour that dont align with my logo
• Over complicated '/ non symmetrical design

```html
<!DOCTYPE html>
<html lang="en">
<head>
<meta charset="utf-8">
<title>Danvir Okelowa Photography — Business Card</title>
<link rel="stylesheet" href="https://fonts.googleapis.com/css2?family=Cinzel:wght@400&family=Open+Sans:wght@400&display=swap">
<style>
  :root {
    --stage: #4a4a4a;
    --card-front: #ffffff;
    --card-back: #000000;
    --taupe: #857763;
    --taupe-soft: #8f8575;
    --ink: #3e3e3e;
    --silver: #c4c4c4;
    --silver-dim: #6e6e6e;
    --faint: #f1f0ee;
  }
  * { margin: 0; padding: 0; box-sizing: border-box; }
  html, body {
    width: 1105px;
    height: 1200px;
    overflow: hidden;
    background: var(--stage);
  }
  .sheet {
    position: relative;
    width: 1105px;
    height: 1200px;
  }
  .card {
    position: absolute;
    left: 192px;
    width: 720px;
    height: 412px;
    overflow: hidden;
  }
  .card--front { top: 146px; background: var(--card-front); }
  .card--back { top: 602px; background: var(--card-back); }

  .card__emblem-faint {
    position: absolute;
    left: 50%;
    top: 50%;
    transform: translate(-50%, -50%);
  }
  .brand {
    position: absolute;
    left: 0;
    width: 100%;
    text-align: center;
    font-family: "Cinzel", serif;
  }
  .brand__name {
    display: block;
    font-size: 30px;
    line-height: 1;
    letter-spacing: 0.5px;
  }
  .brand__sub {
    display: block;
    font-size: 13px;
    letter-spacing: 7px;
    margin-top: 6px;
    padding-left: 7px;
  }
  .card--front .brand { top: 145px; }
  .card--front .brand__name { color: var(--taupe); }
  .card--front .brand__sub { color: var(--taupe-soft); }

  .contact {
    position: absolute;
    left: 0;
    top: 208px;
    width: 100%;
    text-align: center;
    font-family: "Open Sans", sans-serif;
    font-size: 19px;
    line-height: 27px;
    color: var(--ink);
    font-style: normal;
  }

  .card__emblem {
    position: absolute;
    left: 50%;
    top: 88px;
    transform: translateX(-50%);
  }
  .card--back .brand { top: 278px; }
  .card--back .brand__name { color: var(--silver); font-size: 33px; }
  .card--back .brand__sub { color: var(--silver-dim); font-size: 14px; letter-spacing: 9px; padding-left: 9px; }

  .social {
    position: absolute;
    top: 24px;
    right: 24px;
    display: flex;
    align-items: center;
    gap: 6px;
    font-family: "Open Sans", sans-serif;
    font-size: 13px;
    color: var(--silver-dim);
  }
  .social__square {
    width: 14px;
    height: 14px;
    background: var(--silver-dim);
  }
</style>
</head>
<body>
<main class="sheet">
  <section class="card card--front" aria-label="Card front">
    <svg class="card__emblem-faint" width="380" height="380" viewBox="0 0 380 380" aria-hidden="true">
      <circle cx="190" cy="190" r="180" fill="none" stroke="var(--faint)" stroke-width="3"/>
    </svg>
    <div class="brand">
      <span class="brand__name">Danvir Okelowa</span>
      <span class="brand__sub">Photography</span>
    </div>
    <address class="contact">
      07946218305 | info@tavolenstudio.com<br>
      www.tavolenstudio.com
    </address>
  </section>

  <section class="card card--back" aria-label="Card back">
    <div class="social">
      <span class="social__square"></span>
      <span>Sharely</span>
    </div>
    <svg class="card__emblem" width="160" height="160" viewBox="0 0 160 160" aria-hidden="true">
      <circle cx="80" cy="80" r="74" fill="none" stroke="var(--silver)" stroke-width="2"/>
    </svg>
    <div class="brand">
      <span class="brand__name">Danvir Okelowa</span>
      <span class="brand__sub">Photography</span>
    </div>
  </section>
</main>
</body>
</html>
```